Non fiction book cover. The book advises how to get a new job.

The book size will be 20cm high by 13cm wide and I need a front cover which can wrap around to the back. This book has a serious message, but I've tried to make it quite light to read and accessible. So I don't want a cover that is too dour or serious and not frivolous either. At the end of the project, I will need a high resolution 3D image of the book, included as part of the package.<br/>The Title of the book is:- "Past Fifty? Hunting for your new role?<br/>by Colin Marsh-Whitby".<br/>I am thinking of a light yellow background, with a striking image to attract attention. The image and words should be clear and sharp.<br/>Here is the, BACK COVER wording.<br/>"This book tells you clearly and simply the steps that you need to take, to get a job, once you’re over 50.<br/>It advises you on the techniques to use to write a killer CV.<br/>It explains how to ensure that your CV attention.<br/>It shows the best way to approach your local job agency.<br/>It demonstrates the best way to use your network.<br/><br/>This book, written by someone with 30 years’ experience in the recruitment industry, gives you ALL the answers.<br/>Whether you are a top executive or someone after some local part time work, then this book is for you. <br/>With the help of this book you will secure your next position.<br/>

Target Market(s)

UK, over 50s, male and female.

Font styles to use
Serif

Colors
fbee3e

Requirements
Must have
• A clear uncluttered cover.
Should not have
• Fussy and over complicated

```html
<!DOCTYPE html>
<html lang="en">
<head>
<meta charset="utf-8">
<title>Past Fifty? – Book Cover Wrap</title>
<link rel="stylesheet" href="https://fonts.googleapis.com/css2?family=Noto+Serif:wght@700&family=Arimo:wght@400&display=swap">
<style>
  :root {
    --page: #f6f6f6;
    --yellow-light: #fcee14;
    --yellow-mid: #fbe20c;
    --yellow-warm: #f5bd1c;
    --ink: #060808;
  }
  * { margin: 0; padding: 0; box-sizing: border-box; }
  html, body {
    width: 1200px;
    height: 1200px;
    overflow: hidden;
    background: var(--page);
  }
  .canvas {
    position: relative;
    width: 1200px;
    height: 1200px;
  }
  .cover {
    position: absolute;
    top: 23px;
    width: 569px;
    height: 876px;
    overflow: hidden;
    color: var(--ink);
    font-family: "Arimo", Arial, sans-serif;
    background:
      radial-gradient(ellipse 70% 55% at 70% 45%, var(--yellow-light) 0%, var(--yellow-mid) 55%, transparent 100%),
      linear-gradient(135deg, var(--yellow-warm) 0%, var(--yellow-mid) 45%, var(--yellow-light) 70%, var(--yellow-warm) 100%);
  }
  .cover--front { left: 23px; }
  .cover--back { left: 608px; }

  .title {
    position: absolute;
    left: 150px;
    top: 108px;
    font-family: "Noto Serif", Georgia, serif;
    font-weight: 700;
    line-height: 1;
  }
  .title__line1 {
    display: block;
    font-size: 90px;
    letter-spacing: 1px;
    padding-left: 36px;
  }
  .title__line2 {
    display: block;
    font-size: 112px;
    margin-top: 14px;
    letter-spacing: -2px;
  }
  .hero-image {
    position: absolute;
    left: 0;
    top: 367px;
    width: 558px;
    height: 229px;
    background: var(--ink);
    border-radius: 0 60% 50% 0 / 0 45% 55% 0;
  }
  .subtitle {
    position: absolute;
    left: 31px;
    top: 620px;
    font-size: 56px;
    line-height: 54px;
    font-weight: 400;
  }
  .author {
    position: absolute;
    right: 9px;
    bottom: 10px;
    font-size: 12.5px;
  }

  .blurb-lead {
    position: absolute;
    left: 0;
    right: 0;
    top: 183px;
    text-align: center;
    font-size: 25px;
    line-height: 31.5px;
  }
  .benefits {
    position: absolute;
    left: 64px;
    top: 374px;
    list-style: none;
    font-size: 16.5px;
    line-height: 28px;
  }
  .benefits li::before {
    content: "*";
    font-weight: 700;
    margin-right: 8px;
  }
  .blurb-body {
    position: absolute;
    left: 50px;
    width: 470px;
    top: 588px;
    text-align: center;
    font-size: 13.5px;
    line-height: 18.75px;
  }
</style>
</head>
<body>
<main class="canvas">
  <section class="cover cover--front">
    <h1 class="title">
      <span class="title__line1">PAST</span>
      <span class="title__line2">FIFTY?</span>
    </h1>
    <div class="hero-image" role="img" aria-label="Black silhouette of an outstretched open hand reaching in from the left"></div>
    <h2 class="subtitle">Hunting<br>For Your<br>New<br>Role?</h2>
    <p class="author">by Colin Marsh-Whitby</p>
  </section>

  <section class="cover cover--back">
    <p class="blurb-lead">This book tells you clearly and simply<br>the steps that you need to take,<br>to get a job, once you’re over 50.</p>
    <ul class="benefits">
      <li>It advises you on the techniques to use to write a killer CV.</li>
      <li>It explains how to ensure that your CV attention.</li>
      <li>It shows the best way to approach your local job agency.</li>
      <li>It demonstrates the best way to use your network.</li>
    </ul>
    <p class="blurb-body">This book, written by someone with 30 years’ experience in the recruitment industry, gives you ALL the answers. Whether you are a top executive or someone after some local part time work, then this book is for you. with the help of this book you will secure your next position.</p>
  </section>
</main>
</body>
</html>
```